WOMENS REMINDER CARDS

To remind female patients of their yearly exam

Requirements
Must have
• please use only the left side of this picture
also please add a physician Dr. Marcus T. Brandt to the list of physicians.

```html
<!DOCTYPE html>
<html lang="en">
<head>
<meta charset="utf-8">
<title>Reminder Postcard</title>
<link rel="stylesheet" href="https://fonts.googleapis.com/css2?family=Cinzel:wght@400&family=Arimo:wght@400;700&family=Open+Sans:wght@400&display=swap">
<style>
  :root {
    --stage: #000000;
    --card-white: #ffffff;
    --sky-deep: #1f6fe0;
    --sky-mid: #3f8ff0;
    --sky-pale: #cfe4fb;
    --cloud: #eef5fd;
    --brand-navy: #2a2a7a;
    --ink: #1a1a1a;
    --ink-soft: #333333;
    --guide-grey: #c4c4c4;
    --rule: #555555;
  }
  * { margin: 0; padding: 0; box-sizing: border-box; }
  html, body {
    width: 1200px; height: 592px; overflow: hidden;
    background: var(--stage);
  }
  .canvas { position: relative; width: 1200px; height: 592px; }

  .card { position: absolute; top: 35px; width: 546px; height: 432px; overflow: hidden; }
  .card-front { left: 36px; }
  .card-back { left: 621px; background: var(--card-white); }

  /* front */
  .sky-photo {
    position: absolute; inset: 0;
    background:
      radial-gradient(ellipse 40% 22% at 50% 8%, var(--cloud) 0%, rgba(238,245,253,0) 100%),
      radial-gradient(ellipse 22% 20% at 10% 22%, var(--cloud) 0%, rgba(238,245,253,0) 100%),
      radial-gradient(ellipse 25% 25% at 92% 78%, var(--cloud) 0%, rgba(238,245,253,0) 100%),
      radial-gradient(ellipse 60% 18% at 50% 100%, var(--cloud) 0%, rgba(238,245,253,0) 100%),
      linear-gradient(180deg, var(--sky-deep) 0%, var(--sky-mid) 55%, var(--sky-pale) 100%);
  }
  .headline { position: absolute; left: 36px; top: 166px; width: 476px; height: 74px; overflow: visible; }
  .headline text { font-family: "Cinzel", serif; font-size: 90px; fill: var(--card-white); }
  .website {
    position: absolute; left: 0; width: 100%; top: 243px; text-align: center;
    font-family: "Open Sans", sans-serif; font-size: 12.5px; line-height: 17px; letter-spacing: 0.4px;
    color: var(--card-white);
  }
  .brand {
    position: absolute; display: flex; align-items: center; gap: 7px;
    font-family: "Arimo", sans-serif; font-weight: 400; color: var(--brand-navy);
  }
  .brand-dot { border-radius: 50%; background: var(--brand-navy); flex: none; }
  .card-front .brand { left: 36px; top: 358px; font-size: 18px; }
  .card-front .brand-dot { width: 12px; height: 12px; }
  .address {
    position: absolute; right: 26px; top: 368px;
    font-family: "Arimo", sans-serif; font-style: normal; font-size: 12.5px; line-height: 15px;
    color: var(--brand-navy);
  }
  .address .phone { font-size: 14.5px; line-height: 20px; }

  /* back */
  .sky-corner {
    position: absolute; left: 0; top: 0; width: 330px; height: 110px;
    background: radial-gradient(ellipse 80% 100% at 20% 0%, var(--sky-mid) 0%, var(--sky-pale) 45%, rgba(255,255,255,0) 100%);
  }
  .physicians { position: absolute; left: 39px; top: 42px; font-family: "Arimo", sans-serif; }
  .physicians h2 { font-size: 13px; font-weight: 700; color: var(--ink); line-height: 15px; }
  .physicians p { font-size: 12px; color: var(--ink-soft); line-height: 14px; }
  .appointment {
    position: absolute; left: 39px; top: 100px; display: flex; gap: 12px;
    font-family: "Arimo", sans-serif; font-size: 12px; color: var(--ink-soft);
  }
  .appointment .blank { display: inline-block; border-bottom: 1px solid var(--rule); margin-left: 3px; vertical-align: -2px; }
  .card-back .brand { left: 42px; top: 155px; font-size: 14px; }
  .card-back .brand-dot { width: 9px; height: 9px; }
  .guide {
    position: absolute; font-family: "Open Sans", sans-serif; color: var(--guide-grey);
  }
  .guide-postage { right: 28px; top: 24px; font-size: 15px; line-height: 19px; text-align: center; }
  .guide-mailing { left: 330px; top: 236px; font-size: 14px; }
  .guide-no-address { left: 75px; top: 292px; font-size: 12px; }
  .guide-barcode { left: 229px; top: 399px; font-size: 14px; }
</style>
</head>
<body>
<main class="canvas">
  <section class="card card-front" aria-label="Postcard front">
    <div class="sky-photo" role="img" aria-label="Photograph of a bright blue sky with white clouds"></div>
    <svg class="headline" viewBox="0 0 476 74" aria-label="Reminder">
      <text x="0" y="71" textLength="476" lengthAdjust="spacingAndGlyphs">REMINDER</text>
    </svg>
    <p class="website">www.harborwomensclinic.com</p>
    <div class="brand"><span class="brand-dot"></span>Harbor Women's Clinic</div>
    <address class="address">
      1820 Meadowlark Parkway,<br>
      Suite B-210,&nbsp; Riverton, La.<br>
      <span class="phone">70999 (555) 012 4470</span>
    </address>
  </section>

  <section class="card card-back" aria-label="Postcard back">
    <div class="sky-corner" role="img" aria-label="Corner of blue sky with clouds fading into white"></div>
    <div class="physicians">
      <h2>PHYSICIANS</h2>
      <p>Daniel R. Whitcomb, M.D. Peter J. Lowry, M.D. Owen Castillo,<br>
      M.D. Marcus T. Brandt, M.D. Alan F. Brewster, M.D., Dr. Ramsey</p>
    </div>
    <div class="appointment">
      <span>Date:<span class="blank" style="width:98px"></span></span>
      <span>Time:<span class="blank" style="width:100px"></span></span>
    </div>
    <div class="brand"><span class="brand-dot"></span>Harbor Women's Clinic</div>
    <p class="guide guide-postage">Postage<br>Clear<br>Zone</p>
    <p class="guide guide-mailing">Mailing address Area</p>
    <p class="guide guide-no-address">No Address in this area</p>
    <p class="guide guide-barcode">Barcode Area</p>
  </section>
</main>
</body>
</html>
```